Business Card Design for Logistics Startup

Link to my logo source file -
https://www.fylvault.com/sh/qormx7pl2vkc8wd/KLmrT9_ZPq4BnWvHhYtaeCxo?dl=0

We want a statement in our business card!
I have go thru your portfolio, and invites 3 of you guys to design my business card as the previous designer cannot give me the feel.
Let me know if you want any information.
Thanks.
Updates

Target Market(s)

Transport and Logistics
: Shippers, Freight Forwarders and Carriers.

Industry/Entity Type

Business

Contact Information for Business Card

Our details;

Name: Marcus Loh
Designation: General Manager
Mobile: +65 91234508
Email: marcus.loh@corvinmarl.com
Address: 7 Lorong Pelita Rise
RHOMB Tower #09-17
Singapore 639217

Name: Victor Yeo
Designation: Director
Mobile: +65 93416672
Email: victor.yeo@corvinmarl.com
RHOMB Tower #09-17
Singapore 639217

Colors
f37122

Requirements
Must have
• Logo from my source file.
• Please included tagline: Transport and Logistics
• If you guy can think of a tagline - Using E and S, that will be perfect. Such as Excellence in Service..

```html
<!DOCTYPE html>
<html lang="en">
<head>
<meta charset="utf-8">
<title>Corvin Marl Business Card</title>
<link rel="stylesheet" href="https://fonts.googleapis.com/css2?family=Source+Sans+3:wght@400;500&display=swap">
<style>
  :root {
    --backdrop: #e8e8e8;
    --paper-light: #f7f7f6;
    --paper-dark: #1f1e1d;
    --brand-orange: #f37122;
    --ink: #1c1c1c;
    --ink-light: #f2f2f2;
  }
  * { margin: 0; padding: 0; box-sizing: border-box; }
  html, body {
    width: 1200px;
    height: 900px;
    overflow: hidden;
    background: var(--backdrop);
    font-family: "Source Sans 3", sans-serif;
  }
  .canvas { position: relative; width: 1200px; height: 900px; }

  .card {
    position: absolute;
    left: 382px;
    width: 411px;
    height: 253px;
  }
  .card--front { top: 147px; background: var(--paper-light); color: var(--ink); }
  .card--back { top: 473px; background: var(--paper-dark); color: var(--ink-light); }

  .brand {
    position: absolute;
    display: flex;
    flex-direction: column;
    align-items: center;
    gap: 14px;
  }
  .card--front .brand { left: 22px; top: 80px; width: 160px; }
  .card--back .brand { left: 0; top: 80px; width: 411px; }
  .brand__mark {
    width: 42px;
    height: 42px;
    background: var(--brand-orange);
  }
  .brand__name {
    font-size: 15px;
    font-weight: 500;
    letter-spacing: 2.4px;
    white-space: nowrap;
  }

  .divider {
    position: absolute;
    left: 206px;
    top: 66px;
    width: 1.5px;
    height: 123px;
    background: var(--brand-orange);
  }

  .contact {
    position: absolute;
    left: 234px;
    top: 59px;
    font-size: 11.5px;
    line-height: 16px;
  }
  .contact__name {
    color: var(--brand-orange);
    font-size: 15.5px;
    font-weight: 500;
    line-height: 18px;
  }
  .contact__role { font-size: 11.8px; letter-spacing: 0.2px; }
  .contact__lines { margin-top: 14px; }
  .contact__line { display: flex; align-items: center; gap: 3px; }
  .contact__line svg { flex: none; }
  .contact__address { margin-top: 4px; }

  .website {
    position: absolute;
    left: 0;
    top: 200px;
    width: 411px;
    text-align: center;
    font-size: 11.5px;
    letter-spacing: 0.2px;
  }
</style>
</head>
<body>
<div class="canvas">

  <section class="card card--front">
    <div class="brand">
      <div class="brand__mark"></div>
      <div class="brand__name">CORVIN MARL</div>
    </div>
    <div class="divider"></div>
    <div class="contact">
      <div class="contact__name">Marcus Loh</div>
      <div class="contact__role">GENERAL MANAGER</div>
      <div class="contact__lines">
        <div class="contact__line">
          <svg width="9" height="11" viewBox="0 0 9 11" aria-hidden="true">
            <rect x="1.5" y="0.75" width="6" height="9.5" rx="1" fill="none" stroke="#f37122" stroke-width="1.2"/>
            <line x1="3.5" y1="8.6" x2="5.5" y2="8.6" stroke="#f37122" stroke-width="1"/>
          </svg>
          <span>+65 9123 4508</span>
        </div>
        <div class="contact__line">
          <svg width="11" height="9" viewBox="0 0 11 9" aria-hidden="true">
            <rect x="0.5" y="1" width="10" height="7" fill="#f37122"/>
            <polyline points="0.5,1.3 5.5,5 10.5,1.3" fill="none" stroke="#f7f7f6" stroke-width="0.9"/>
          </svg>
          <span>marcus.loh@corvinmarl.com</span>
        </div>
      </div>
      <div class="contact__address">
        <div>7 Lorong Pelita Rise</div>
        <div>RHOMB Tower #09-17</div>
        <div>Singapore 639217</div>
      </div>
    </div>
  </section>

  <section class="card card--back">
    <div class="brand">
      <div class="brand__mark"></div>
      <div class="brand__name">CORVIN MARL</div>
    </div>
    <div class="website">www.corvinmarl.com</div>
  </section>

</div>
</body>
</html>
```